New Corporate Business Card - Velmorana

What we need:
We need a new corporate business card.
We want a new template that we can change by ourself.
We want business card modern and minimalist but that looks professional.
We will print it in 300 gr soft-touch.
Why not a white side with the logo and a red/grey side with the content?
Why not a grey side and a red side like our logo?
I am sure that you have better idea than ours that's the reason we come here.

Who we are:
We are a private label company in cosmetics based in Switzerland. We work in BtoB. We make skin care products for other brands.

Target Market(s)

B to B - Worldwide - any gender

Industry/Entity Type

Cosmetics

Contact Information for Business Card

Side 1:
Logo
Your Swiss Private Label Manufacturer or www.velmorana-example.ch

Side 2:
Name and surname (Example: Lucien Marchetaz)
Job Description (General Manager)
Telephone (+41 32 915 63 00)
Direct (+41 32 915 63 63)
Email (lucien.marchetaz@velmorana-example.ch)
Chemin des Pélerines 14, 2000 Neuchâtel, Switzerland
www.velmorana-example.ch

Font styles to use
Serif
Sans Serif

Requirements
Must have
• You can use 4 colors: white, red, grey and/or black .
Should not have
• Too much colors, too much things. We want it simple!

```html
<!DOCTYPE html>
<html lang="en">
<head>
<meta charset="utf-8">
<title>Velmorana – Business Card</title>
<link rel="stylesheet" href="https://fonts.googleapis.com/css2?family=Jost:wght@400;500&family=Roboto:wght@400;700&display=swap">
<style>
  :root {
    --red: #ee2d24;
    --grey: #a7a8ab;
    --ink: #1d1d1b;
    --white: #ffffff;
    --backdrop: #e9e9ea;
  }
  * { margin: 0; padding: 0; box-sizing: border-box; }
  html, body { width: 1200px; height: 1000px; overflow: hidden; }
  body {
    background: var(--backdrop);
    position: relative;
    font-family: "Jost", sans-serif;
    color: var(--ink);
  }
  .card {
    position: absolute;
    width: 620px;
    height: 400px;
    border-radius: 26px;
    overflow: hidden;
    box-shadow: 0 10px 30px rgba(0,0,0,.18);
  }
  .card-back {
    left: 480px; top: 60px;
    background: var(--red);
    display: flex; align-items: center; justify-content: center;
  }
  .card-back .brand-name {
    font-family: "Jost", sans-serif;
    font-weight: 400;
    font-size: 64px;
    letter-spacing: 6px;
    color: var(--white);
  }
  .card-front {
    left: 100px; top: 540px;
    background: var(--white);
  }
  .card-front .brand-name {
    position: absolute; left: 40px; top: 34px;
    font-family: "Jost", sans-serif;
    font-weight: 400;
    font-size: 44px;
    letter-spacing: 4px;
    color: var(--red);
  }
  .person { position: absolute; left: 40px; top: 150px; font-family: "Roboto", sans-serif; }
  .person-name { font-weight: 700; font-size: 22px; color: var(--red); text-transform: uppercase; }
  .person-role { font-size: 15px; color: var(--ink); margin-top: 2px; }
  .divider {
    position: absolute; left: 40px; top: 202px;
    width: 545px; height: 2px; background: var(--red);
  }
  .address {
    position: absolute; left: 40px; top: 216px;
    font-family: "Roboto", sans-serif; font-size: 14px; line-height: 1.45;
  }
  .phones {
    position: absolute; left: 250px; top: 216px;
    font-family: "Roboto", sans-serif; font-size: 14px; line-height: 1.45;
  }
  .phones .label { color: var(--red); }
  .online {
    position: absolute; right: 35px; top: 262px;
    font-size: 14px; line-height: 1.55;
  }
  .online li { list-style: none; display: flex; align-items: center; gap: 6px; }
  .online svg { width: 12px; height: 12px; flex: none; }
  .bands { position: absolute; left: 0; bottom: 0; width: 620px; height: 90px; }
</style>
</head>
<body>

<section class="card card-back" aria-label="Card back">
  <span class="brand-name">Velmorana</span>
</section>

<section class="card card-front" aria-label="Card front">
  <span class="brand-name">Velmorana</span>

  <div class="person">
    <p class="person-name">Lucien Marchetaz</p>
    <p class="person-role">General Manager</p>
  </div>

  <div class="divider"></div>

  <p class="address">Chemin des Pélerines 14,<br>2000 Neuchâtel, Switzerland</p>

  <p class="phones">
    <span class="label">Tel:</span> +41 32 915 63 00<br>
    <span class="label">Direct:</span> +41 32 915 63 63
  </p>

  <ul class="online">
    <li>
      <svg viewBox="0 0 12 12"><rect x="0.5" y="2" width="11" height="8" rx="1" fill="var(--red)"/><path d="M1 3 L6 7 L11 3" stroke="#fff" stroke-width="1" fill="none"/></svg>
      lucien.marchetaz@velmorana-example.ch
    </li>
    <li>
      <svg viewBox="0 0 12 12"><circle cx="6" cy="6" r="5.5" fill="var(--red)"/><path d="M0.5 6 H11.5 M6 0.5 V11.5 M6 0.5 C3 3 3 9 6 11.5 M6 0.5 C9 3 9 9 6 11.5" stroke="#fff" stroke-width="0.8" fill="none"/></svg>
      www.velmorana-example.ch
    </li>
  </ul>

  <svg class="bands" viewBox="0 0 620 90" preserveAspectRatio="none">
    <path d="M0 8 H255 Q268 8 275 22 L280 32 H620 V90 H0 Z" fill="var(--grey)"/>
    <path d="M0 20 H265 Q278 20 285 38 L290 48 H620 V90 H0 Z" fill="var(--red)"/>
  </svg>
</section>

</body>
</html>
```